The Bridgework Prism - A coaching tool for high level sales people

I would like a design for a professional development tool called The Bridgework Prism. I will use this tool in powerpoint presentations and with individual coaching clients to help them understand how to connect with people quickly. I would like the triangle to be the infinity triangle that I have attached and for the sides of the triangle to be called Emotional Intelligence, Social Intelligence and Practical Empathy. Inside the triangle should be the word trust. For colours and style, see our logo, attached and our website www.meadowlarkpropertyguild.example It should be professional but natural and a touch of whimsy may work well.

Target Market(s)

Real Estate Agents in Canada and the US who are open to professional development

Industry/Entity Type

Real Estate

Font styles to use
Sans Serif

Colors
32a6d6
85acd3
3176b5
0858a5
85cae6
85abd2
ec1f27

Requirements
Must have
• must have a great feel. We are called The Meadowlark Property Guild because we find ways for salespeople to excel in sales using their natural strengths, having authentic conversations and understanding their clients and customers in a deep and meaningful way. The colours should align with our branding as per the website.
Nice to have
• It should come across as professional but not too formal. A subtle sense of nature would be a benefit/
Should not have
• Should not be bold and should not use colours not used in our branding

```html
<!DOCTYPE html>
<html lang="en">
<head>
<meta charset="utf-8">
<title>The Bridgework Prism</title>
<link rel="stylesheet" href="https://fonts.googleapis.com/css2?family=Fira+Sans+Condensed:wght@500;600;800&family=Fira+Sans+Extra+Condensed:wght@500&display=swap">
<style>
  :root {
    --paper: #eeeff0;
    --ink: #2e2a2a;
    --sky: #0ea5d8;
    --deep: #1670b7;
    --mist: #42bdf0;
    --ember: #ec1f27;
    --label: #ffffff;
  }
  html, body {
    margin: 0;
    padding: 0;
    width: 849px;
    height: 1200px;
    overflow: hidden;
    background: var(--paper);
  }
  .poster {
    position: relative;
    width: 849px;
    height: 1200px;
    background: var(--paper);
    font-family: "Fira Sans Condensed", "Arial Narrow", sans-serif;
    color: var(--ink);
  }
  .poster-title {
    position: absolute;
    top: 72px;
    left: 0;
    width: 100%;
    margin: 0;
    text-align: center;
    font-weight: 600;
    line-height: 1;
  }
  .poster-title .title-kicker {
    display: block;
    font-size: 33px;
    letter-spacing: 1px;
  }
  .poster-title .title-main {
    display: block;
    margin-top: 12px;
    font-size: 96px;
    letter-spacing: 3px;
  }
  .prism {
    position: absolute;
    top: 0;
    left: 0;
  }
  .region-emotional { fill: var(--sky); }
  .region-practical { fill: var(--deep); }
  .region-social { fill: var(--mist); }
  .seam-glow { fill: none; stroke: var(--ember); stroke-width: 13; }
  .seam-shade { fill: none; stroke: var(--ink); stroke-width: 8; }
  .core { fill: var(--paper); }
  .core-word {
    font-family: "Fira Sans Condensed", "Arial Narrow", sans-serif;
    font-weight: 800;
    font-size: 60px;
    letter-spacing: 2px;
    fill: var(--ink);
  }
  .side-label {
    font-family: "Fira Sans Extra Condensed", "Arial Narrow", sans-serif;
    font-weight: 500;
    font-size: 28px;
    letter-spacing: 2px;
    fill: var(--label);
  }
  .guild-name {
    position: absolute;
    top: 1032px;
    left: 0;
    width: 100%;
    margin: 0;
    display: flex;
    justify-content: center;
    align-items: center;
    gap: 14px;
    font-weight: 600;
    font-size: 30px;
    color: var(--ink);
  }
  .guild-mark {
    width: 18px;
    height: 18px;
    border-radius: 50%;
    background: var(--ink);
  }
</style>
</head>
<body>
<main class="poster">
  <h1 class="poster-title">
    <span class="title-kicker">THE BRIDGEWORK</span>
    <span class="title-main">PRISM</span>
  </h1>

  <svg class="prism" width="849" height="1200" viewBox="0 0 849 1200" aria-label="Prism of emotional intelligence, practical empathy and social intelligence around trust">
    <defs>
      <clipPath id="prism-outline">
        <path d="M373.6,349.7 Q424,252 474.1,349.9 L694.9,782.1 Q745,880 635,880 L210,880 Q100,880 150.4,782.3 Z"/>
      </clipPath>
      <path id="sector" d="M0,95 A157,157 0 0 1 -177,-60 L-500,-60 L-400,-500 L301,-403 L140.4,-123.4 A157,157 0 0 0 -82.3,-47.5 A95,95 0 0 0 0,95 Z"/>
      <path id="seam" d="M0,95 A157,157 0 0 1 -177,-60 L-260,-60"/>
      <path id="arc-emotional" d="M299.3,687.6 A174,174 0 0 1 574.7,483.8"/>
      <path id="arc-practical" d="M442.6,953.8 A242,242 0 0 0 401.1,478.9"/>
      <path id="arc-social" d="M165.8,498.4 A267,267 0 0 0 631.0,743.7"/>
    </defs>

    <g clip-path="url(#prism-outline)">
      <g transform="translate(420 645)">
        <use href="#sector" class="region-emotional"/>
        <use href="#sector" class="region-practical" transform="rotate(120)"/>
        <use href="#sector" class="region-social" transform="rotate(240)"/>

        <g class="seams">
          <g>
            <use href="#seam" class="seam-glow"/>
            <use href="#seam" class="seam-shade" transform="translate(-2 -2)"/>
          </g>
          <g transform="rotate(120)">
            <use href="#seam" class="seam-glow"/>
            <use href="#seam" class="seam-shade" transform="translate(-2 -2)"/>
          </g>
          <g transform="rotate(240)">
            <use href="#seam" class="seam-glow"/>
            <use href="#seam" class="seam-shade" transform="translate(-2 -2)"/>
          </g>
        </g>

        <circle class="core" cx="0" cy="0" r="95"/>
      </g>
    </g>

    <text class="core-word" x="420" y="666" text-anchor="middle">TRUST</text>

    <text class="side-label"><textPath href="#arc-emotional" startOffset="50%" text-anchor="middle">EMOTIONAL INTELLIGENCE</textPath></text>
    <text class="side-label"><textPath href="#arc-practical" startOffset="50%" text-anchor="middle">PRACTICAL EMPATHY</textPath></text>
    <text class="side-label"><textPath href="#arc-social" startOffset="50%" text-anchor="middle">SOCIAL INTELLIGENCE</textPath></text>
  </svg>

  <p class="guild-name"><span class="guild-mark"></span>The Meadowlark Property Guild</p>
</main>
</body>
</html>
```